Tova Meadows brand , chocolate packaging design

Tova Meadows

Products List

CANNABIS INFUSED CHOCOLATE BAR
(4 Flavor Chocolate Bar)
Original Milk chocolate Bar
Cookies N Cream Bar
Strawberry Cheesecake Bar
S’mores Bar

Information Front
-1000 MG THC Per package
-100mg THC per serving
-Made with Belgian Chocolate
-Made with Quality California Cannabis Extracts
-Net weight of bar 50grams
-California triangle warning symbol
-Flavor of chocolate bar

Information Back

-10 Servings per package
-100 mg serving size

-Directions
Wait 1-2 hours for full effect before consuming more.
-Very potent , Keep out of reach of children

-Store at 68-77° F
-Will melt in prolonged heat
-California government warning and ad41notice website

Ingredient list

Milk chocolate Bar
MILK CHOCOLATE (SUGAR, COCOA BUTTER , UNSWEETENED CHOCOLATE, SUNFLOWER LECITHIN, VANILLA) , CANNABIS EXTRACT.
ALLERGENS-CONTAINS MILK

Strawberry Cheesecake
WHITE CHOCOLATE (SUGAR, COCOA BUTTER, WHOLE MILK POWDER ,SOY LECITHIN, NATURAL VANILLA FLAVOR) STRAWBERRY POWDER , STRAWBERRY EXTRACT , NATURAL FLAVORS, CANNABIS EXTRACT.

Cookies n cream
WHITE CHOCOLATE (SUGAR, COCOA BUTTER, WHOLE MILK POWDER ,SOY LECITHIN, NATURAL VANILLA FLAVOR) 9
KRUNDELS (SUGAR, WHITE RICE FLOUR, TAPIOCA STARCH, PALM OIL, CANOLA OIL, WHOLE OAT FLOUR, CORN STARCH , COCOA (PROCESSED WITH ALKALI), INVERT SUGAR, SOY LECITHIN, BAKING SODA, SALT, XANTHAM GUM , CHOCOLATE, ARTIFICIAL FLAVOR, CANNABIS EXTRACT

S’mores
MILK CHOCOLATE (SUGAR, COCOA BUTTER, MILK, UNSWEETENED CHOCOLATE ,SUNFLOWER LECITHIN, VANILLA), MARSHMALLOW (SUGAR ,CORN SYRUP , MODIFIED STARCH, GELATIN, SODIUM HEXAMETAPHOSPHATE, ARTIFICIAL FLAVOR , NATURAL FLAVOR , ARTIFICIAL COLO (BLUE 1)), GRAHAM CRACKER (CORN STARCH, BROWN SUGAR , CORN FLOUR, PALM FAT , SOY FLOUR , SOY BRAN, HONEY, MODIFIED TAPIOCA STARCH, AMMONIUM BICARBONATE, BAKING SODA, SALT, CARAMELIZED SUGAR) NATURAL FLAVOR, CANNABIS EXTRACT.

Looking for simple clean modern design , chocolate bar can be like marivel of like the Brisbury one with images on it , and gummy is a mylar bag I really like the Brisbury style , I can provide dieline etc thank you !

Target Market(s)

Young adults

Industry/Entity Type

Cannabis , Delta 8 , CBD

Requirements
Must have
• Chocolate bar is box , dielines Included with images
Nice to have
• Simple clean , elegant and modern design , like the marivel and Brisbury brands , white logo preferred

```html
<!DOCTYPE html>
<html lang="en">
<head>
<meta charset="UTF-8">
<title>Tova Meadows – S'mores Chocolate Bar</title>
<link href="https://fonts.googleapis.com/css2?family=Oswald:wght@300;400&family=Allura&display=swap" rel="stylesheet">
<style>
  :root {
    --bg: #d6d6d6;
    --panel-dark: #353535;
    --panel-dark-top: #474747;
    --cream: #ddd1c1;
    --cream-deep: #d5c7b4;
    --ink: #2e2e2e;
    --white: #f4f2ee;
    --accent: #dccfbd;
  }
  * { margin: 0; padding: 0; box-sizing: border-box; }
  html, body { width: 1175px; height: 1200px; overflow: hidden; background: var(--bg); }
  .canvas { position: relative; width: 1175px; height: 1200px; }

  .bar-wrap {
    position: absolute; left: 388px; top: 126px; width: 408px; height: 972px;
    font-family: "Oswald", sans-serif; text-align: center;
  }
  .front-dark {
    position: absolute; left: 0; top: 0; width: 100%; height: 741px;
    background: linear-gradient(160deg, var(--panel-dark-top), var(--panel-dark) 60%);
  }
  .front-cream {
    position: absolute; left: 0; top: 741px; width: 100%; height: 231px;
    background: linear-gradient(180deg, var(--cream), var(--cream-deep));
  }
  .tab {
    position: absolute; left: 183px; top: 2px; width: 42px; height: 54px;
    background: var(--accent);
  }
  .brand {
    position: absolute; left: 0; right: 0; top: 88px;
    color: var(--white); font-weight: 400; font-size: 46px; letter-spacing: 3px;
    line-height: 1; padding-left: 14px;
  }
  .product-name {
    position: absolute; left: 0; right: 0; top: 326px;
    color: var(--white); font-weight: 400; font-size: 31px; letter-spacing: 3px; line-height: 46px;
  }
  .dots {
    position: absolute; left: 0; right: 0; top: 452px;
    display: flex; justify-content: center; gap: 6px;
  }
  .dots span { width: 5px; height: 5px; border-radius: 50%; background: var(--accent); }
  .potency {
    position: absolute; left: 0; right: 0; top: 486px; color: var(--white);
    display: flex; justify-content: center; padding-left: 8px;
  }
  .potency .col { display: flex; flex-direction: column; align-items: center; }
  .potency .amount { font-size: 24px; letter-spacing: 1px; line-height: 30px; }
  .potency .unit { font-size: 14px; font-weight: 300; letter-spacing: 2px; line-height: 22px; }
  .potency .sep { width: 1px; background: var(--white); height: 22px; margin: 5px 6px 0; }
  .potency .sep.small { height: 14px; }
  .flavor {
    position: absolute; left: 0; right: 0; top: 592px;
    font-family: "Allura", cursive; font-size: 52px; color: var(--accent); line-height: 1;
  }
  .flavor-art {
    position: absolute; left: 122px; top: 669px; width: 177px; height: 123px;
    border-radius: 10px;
    background: radial-gradient(ellipse at 50% 50%, #f2ece3 0%, #b98a55 45%, #4a2e22 80%, rgba(74,46,34,0) 100%);
  }
  .claim {
    position: absolute; left: 0; right: 0; top: 814px;
    color: var(--ink); font-size: 15px; letter-spacing: 1.6px; padding-left: 18px;
  }
  .rule {
    position: absolute; left: 111px; top: 849px; width: 176px; height: 2px; background: var(--ink);
  }
  .origin {
    position: absolute; left: 90px; right: 0; top: 865px;
    color: var(--ink); font-size: 15px; letter-spacing: 1.6px; text-align: left;
  }
  .weight {
    position: absolute; left: 98px; top: 899px; width: 202px; height: 31px;
    background: var(--ink); color: var(--cream); font-size: 16px; letter-spacing: 2px;
    line-height: 31px;
  }
  .compliance-badge {
    position: absolute; left: 22px; top: 872px; width: 56px; height: 56px;
    border: 4px solid var(--ink);
  }
</style>
</head>
<body>
<div class="canvas">
  <div class="bar-wrap">
    <div class="front-dark"></div>
    <div class="front-cream"></div>
    <div class="tab"></div>

    <h1 class="brand">TOVA MEADOWS</h1>
    <p class="product-name">CANNABIS INFUSED<br>CHOCOLATE BAR</p>
    <div class="dots"><span></span><span></span><span></span></div>

    <div class="potency">
      <div class="col">
        <span class="amount">1000 MG THC</span>
        <span class="unit">PER PACKAGE</span>
      </div>
      <div class="col">
        <span class="sep"></span>
        <span class="sep small"></span>
      </div>
      <div class="col">
        <span class="amount">100MG THC</span>
        <span class="unit">PER SERVING</span>
      </div>
    </div>

    <p class="flavor">S’mores</p>
    <div class="flavor-art" role="img" aria-label="Illustration of two s'mores with graham crackers, marshmallow and melted chocolate"></div>

    <p class="claim">WITH QUALITY CALIFORNIA CANNABIS EXTRACTS</p>
    <div class="rule"></div>
    <p class="origin">MADE WITH BELGIAN CHOCOLATE</p>
    <div class="weight">NET WEIGHT: 50GRAMS</div>

    <div class="compliance-badge" role="img" aria-label="Regulatory warning badge"></div>
  </div>
</div>
</body>
</html>
```